Food Festival "Signature Cocktail" Booth Banner

Need a 3'x9'6" (36" tall x 114" wide) Outdoor Banner for a new "Signature Cocktail" booth at an outdoor food festival. Pellston Onion Jubilee is a non profit festival and the World Record largest Garlic Festival with average of 100K attendees over 3 days. Actual drink served will vary from year to year, but banner for the booth with be reused each year so it will be non drink specific. Banner needs to catch attendee's attention both at a quick glance and from a distance outdoors to drive traffic and sales to the booth. It will be mounted above the sales window of a 10x10 Festival Booth on PVC frame (see attached pic for reference). "Signature Cocktail" is required text along with it being identified as a Pellston Onion Jubilee booth either through use of attached logo (color can be modified) or "Pellston Onion Jubilee" text since we also have for profit competing vendors. Banner will be full color print. Idea concepts: Neon Sign, Art Deco elegant, reclaimed wood...but open to any concepts. Festival website: https://pellstononionjubilee.example

Target Market(s)

Food Festival Attendees

Font styles to use
Decorative
Script
Other font styles liked:
• Neon, heavy weight fonts, open.

Colors

Designer to choose colors to be used in the design.

Requirements
Must have
• "Signature Cocktail" and "Pellston Onion Jubilee" text or POJ Logo provided, colors and layout that stands out and easily identifiable and readable from a long distance with strong text
Nice to have
• Vibrant engaging background,, ties to Garlic
Should not have
• Clip art, generic text

```html
<!DOCTYPE html>
<html lang="en">
<head>
<meta charset="utf-8">
<title>Signature Cocktail – Pellston Onion Jubilee Booth Banner</title>
<link href="https://fonts.googleapis.com/css2?family=Great+Vibes&family=Montserrat:wght@800;900&display=swap" rel="stylesheet">
<style>
  :root {
    --wood-white: #f7f6f4;
    --wood-seam: #dcdad6;
    --splash-pink: #f3a6cf;
    --splash-pink-soft: #fbd3e6;
    --splash-orange: #f59a6b;
    --script-magenta: #e2137f;
    --script-shadow: #8e1050;
    --headline-black: #0c0c0c;
    --headline-edge: #e2137f;
    --brand-ink: #1a1a1a;
  }
  html, body {
    margin: 0;
    padding: 0;
    width: 1200px;
    height: 379px;
    overflow: hidden;
    background: var(--wood-white);
  }
  .banner {
    position: relative;
    width: 1200px;
    height: 379px;
    overflow: hidden;
    background: var(--wood-white);
  }
  .banner__art {
    position: absolute;
    inset: 0;
    width: 1200px;
    height: 379px;
    display: block;
  }
  .brand {
    position: absolute;
    left: 24px;
    top: 40px;
    width: 190px;
    height: 200px;
    display: flex;
    flex-direction: column;
    align-items: center;
    justify-content: center;
    gap: 10px;
  }
  .brand__dot {
    width: 60px;
    height: 60px;
    border-radius: 50%;
    background: var(--brand-ink);
  }
  .brand__name {
    margin: 0;
    font-family: "Montserrat", sans-serif;
    font-weight: 900;
    font-size: 22px;
    line-height: 1.1;
    letter-spacing: 1px;
    text-transform: uppercase;
    text-align: center;
    color: var(--brand-ink);
  }
  .title-script {
    font-family: "Great Vibes", cursive;
    fill: var(--script-magenta);
  }
  .title-script--shadow { fill: var(--script-shadow); }
  .title-block {
    font-family: "Montserrat", sans-serif;
    font-weight: 900;
    fill: var(--headline-black);
  }
  .title-block--edge { fill: var(--headline-edge); }
</style>
</head>
<body>
<main class="banner">
  <svg class="banner__art" viewBox="0 0 1200 379" xmlns="http://www.w3.org/2000/svg">
    <defs>
      <linearGradient id="splashTone" x1="0" y1="0" x2="1" y2="0.3">
        <stop offset="0" stop-color="var(--splash-pink)"/>
        <stop offset="0.45" stop-color="var(--splash-pink-soft)"/>
        <stop offset="0.7" stop-color="var(--splash-orange)" stop-opacity="0.75"/>
        <stop offset="1" stop-color="var(--splash-pink)"/>
      </linearGradient>
    </defs>

    <g class="wood-planks">
      <rect width="1200" height="379" fill="var(--wood-white)"/>
      <line x1="0" y1="12" x2="1200" y2="12" stroke="var(--wood-seam)" stroke-width="2"/>
      <line x1="0" y1="62" x2="1200" y2="62" stroke="var(--wood-seam)" stroke-width="2"/>
      <line x1="0" y1="112" x2="1200" y2="112" stroke="var(--wood-seam)" stroke-width="2"/>
      <line x1="0" y1="162" x2="1200" y2="162" stroke="var(--wood-seam)" stroke-width="2"/>
      <line x1="0" y1="212" x2="1200" y2="212" stroke="var(--wood-seam)" stroke-width="2"/>
      <line x1="0" y1="262" x2="1200" y2="262" stroke="var(--wood-seam)" stroke-width="2"/>
      <line x1="0" y1="312" x2="1200" y2="312" stroke="var(--wood-seam)" stroke-width="2"/>
      <line x1="0" y1="362" x2="1200" y2="362" stroke="var(--wood-seam)" stroke-width="2"/>
    </g>

    <path class="splash" role="img" aria-label="Flowing pink and orange cocktail splash with bubbles sweeping across the banner"
      fill="url(#splashTone)" opacity="0.85"
      d="M0 300 C60 250 140 280 210 300 C300 325 300 250 380 200 C470 140 560 60 680 40 C760 28 820 0 880 0 L940 0 C880 40 820 80 760 110 C860 120 960 170 1040 200 C1110 225 1160 250 1200 262 L1200 300 C1140 290 1060 280 980 300 C900 320 820 340 720 330 C640 322 600 300 540 330 C480 360 420 379 360 379 L0 379 Z"/>

    <g class="headline">
      <text class="title-block title-block--edge" y="354" font-size="115" x="219 347 487 615 747 864 1000 1077">COCKTAIL</text>
      <text class="title-block" y="351" font-size="115" x="216 344 484 612 744 861 997 1074">COCKTAIL</text>
      <text class="title-script title-script--shadow" x="267" y="235" font-size="190" textLength="800" lengthAdjust="spacingAndGlyphs">Signature</text>
      <text class="title-script" x="264" y="232" font-size="190" textLength="800" lengthAdjust="spacingAndGlyphs">Signature</text>
    </g>
  </svg>

  <div class="brand">
    <span class="brand__dot" aria-hidden="true"></span>
    <p class="brand__name">Pellston<br>Onion<br>Jubilee</p>
  </div>
</main>
</body>
</html>
```